Modern Business Card for Lanternfield 2018

Our company assumes the best about people. We are creating an online community of entrepreneurs and business leaders who struggle with marketing their business online.

This business card should POP! We recently got a new logo and are launching a new website next month, so our business cards should make a statement that feels:
-Fresh
-Smart
-Trustworthy
-Fun

Target Market(s)

small business owners, entrepreneurs

Industry/Entity Type

Digital Marketing

Contact Information for Business Card

Dimensions: 3.5" x 2"

Font styles to use
Sans Serif

Colors
f37122
ffffff

Requirements
Must have
• We need a business card with a modern, bold design. We will use one side of the card as a lead-generation offer, so text on one side will need to fit up to 140 characters. The business card should stick to our core colors (orange, black, and white).
Nice to have
• We think a vertical "portrait" design could be interesting.
Should not have
• Should not look like a traditional business card. The round icon should stand out from a distance.

```html
<!DOCTYPE html>
<html lang="en">
<head>
<meta charset="UTF-8">
<title>Lanternfield – Business Card</title>
<link href="https://fonts.googleapis.com/css2?family=Montserrat:wght@800&family=Open+Sans:wght@400;700&family=Permanent+Marker&family=Caveat:wght@400&display=swap" rel="stylesheet">
<style>
  :root {
    --orange: #ff8200;
    --peach: #fdd0a0;
    --ink: #1c1c1c;
    --white: #ffffff;
  }
  html, body {
    margin: 0;
    padding: 0;
    overflow: hidden;
    background: var(--white);
  }
  .card {
    position: relative;
    width: 1200px;
    height: 982px;
    background: var(--white);
    overflow: hidden;
  }
  .header-shape {
    position: absolute;
    left: 0;
    top: 0;
  }
  .role {
    position: absolute;
    left: 0;
    width: 569px;
    top: 158px;
    margin: 0;
    text-align: center;
    font-family: "Montserrat", sans-serif;
    font-weight: 800;
    font-size: 28px;
    letter-spacing: 0.2px;
    color: var(--white);
  }
  .person-name {
    position: absolute;
    left: 0;
    width: 569px;
    top: 190px;
    margin: 0;
    text-align: center;
    font-family: "Permanent Marker", cursive;
    font-size: 66px;
    line-height: 1;
    color: var(--ink);
    letter-spacing: 1px;
  }
  .brand-dot {
    position: absolute;
    left: 202px;
    top: 532px;
    width: 166px;
    height: 166px;
    border-radius: 50%;
    background: var(--orange);
  }
  .brand-name {
    position: absolute;
    left: 0;
    width: 569px;
    top: 722px;
    margin: 0;
    text-align: center;
    font-family: "Open Sans", sans-serif;
    font-weight: 700;
    font-size: 60px;
    line-height: 1;
    color: var(--ink);
    letter-spacing: 1px;
  }
  .tagline {
    position: absolute;
    left: 0;
    width: 569px;
    top: 806px;
    margin: 0;
    text-align: center;
    font-family: "Caveat", cursive;
    font-size: 34px;
    letter-spacing: 3px;
    color: var(--ink);
    text-transform: uppercase;
    font-style: normal;
  }
  .contact-band {
    position: absolute;
    left: 0;
    top: 889px;
    width: 569px;
    height: 93px;
    background: var(--orange);
    display: flex;
    align-items: center;
    justify-content: center;
  }
  .email {
    font-family: "Open Sans", sans-serif;
    font-size: 34px;
    color: var(--white);
    padding-left: 20px;
  }
  .back-circle {
    position: absolute;
    left: 717px;
    top: 274px;
    width: 430px;
    height: 430px;
    border-radius: 50%;
    background: var(--peach);
  }
</style>
</head>
<body>
  <main class="card">
    <svg class="header-shape" width="569" height="445" viewBox="0 0 569 445" aria-hidden="true">
      <rect x="0" y="0" width="569" height="91" fill="var(--orange)"/>
      <rect x="0" y="94" width="569" height="2" fill="var(--orange)" opacity="0"/>
      <path d="M0 95 H569 V307 C470 380 330 430 150 440 C90 442 40 438 0 425 Z" fill="var(--orange)"/>
    </svg>

    <p class="role">STORY MARKETING COACH</p>
    <h1 class="person-name">DANA WHITLEY</h1>

    <div class="brand-dot" aria-hidden="true"></div>
    <h2 class="brand-name">LANTERNFIELD</h2>
    <p class="tagline">Tell stories that inspire action</p>

    <div class="contact-band">
      <span class="email">dana@lanternfieldnow.com</span>
    </div>

    <div class="back-circle" aria-hidden="true"></div>
  </main>
</body>
</html>
```